Wirelumo

I'm looking to much improve our current website wirelumo.com
Updates

Low design quality

Target Market(s)

Commercial clients (Not-Residentials)

Industry/Entity Type

Office buildings and Industrial clients

Coding

Coded - Design and coding required

Number of Pages Required

5+ page

Requirements
Must have
• Very professional structured low voltage cabling projects for Wi-Fi, Audio/Video conference rooms, Access Control systems, CCTV.

```html
<!DOCTYPE html>
<html lang="en">
<head>
<meta charset="utf-8">
<title>Wirelumo — Commercial Low-Voltage Cabling</title>
<link href="https://fonts.googleapis.com/css2?family=Archivo:wght@400;500;600;700;800;900&family=IBM+Plex+Mono:wght@400;500&display=swap" rel="stylesheet">
<style>
:root{
  --bg:#111113;
  --bg-alt:#18181b;
  --bg-deep:#0c0c0e;
  --panel:#1c1c20;
  --line:#2a2a2f;
  --red:#e11d2a;
  --red-soft:#3a1417;
  --text:#f3f3f4;
  --muted:#9a9aa2;
  --dim:#5f5f67;
}
*{margin:0;padding:0;box-sizing:border-box}
html,body{width:1200px;height:4573px;overflow:hidden;background:var(--bg);color:var(--text);font-family:"Archivo",sans-serif}
.mono{font-family:"IBM Plex Mono",monospace;text-transform:uppercase;letter-spacing:.14em}
.wrap{width:784px;margin:0 auto;position:relative}
.eyebrow{font-family:"IBM Plex Mono",monospace;font-size:9px;letter-spacing:.2em;text-transform:uppercase;color:var(--red);display:flex;align-items:center;gap:8px}
.eyebrow::before{content:"";width:18px;height:1px;background:var(--red)}
.eyebrow.center{justify-content:center}
h2{font-weight:800;font-size:31px;line-height:1.03;letter-spacing:-.02em}
.btn{display:inline-flex;align-items:center;gap:8px;height:40px;padding:0 22px;font-size:11px;font-weight:600;border-radius:2px}
.btn-red{background:var(--red);color:#fff}
.btn-ghost{border:1px solid var(--line);color:var(--text)}
.icon-box{width:30px;height:30px;border:1px solid #5a1b20;background:var(--red-soft);display:flex;align-items:center;justify-content:center;border-radius:2px}
.icon-box svg{width:14px;height:14px;stroke:var(--red);fill:none;stroke-width:1.6}
.tick{width:10px;height:10px;stroke:var(--red);fill:none;stroke-width:2.2;flex:none}

/* nav */
.nav{height:50px;background:var(--bg-deep);border-bottom:1px solid var(--line)}
.nav .wrap{display:flex;align-items:center;height:50px}
.logo{display:flex;align-items:center;gap:6px;font-weight:800;font-size:15px;color:var(--text)}
.logo i{width:12px;height:12px;background:var(--red);display:block}
.nav ul{list-style:none;display:flex;gap:30px;margin-left:100px;font-size:11px;color:var(--muted)}
.nav .phone{margin-left:auto;font-size:11px;display:flex;gap:7px;align-items:center;margin-right:18px}
.nav .phone svg{width:12px;height:12px;stroke:var(--red);fill:none;stroke-width:1.8}
.nav .btn{height:34px;padding:0 18px}

/* hero */
.hero{height:580px;position:relative;background:radial-gradient(ellipse at 80% 30%,#2a1012 0%,transparent 55%),var(--bg);border-bottom:1px solid var(--line);overflow:hidden}
.hero .grid-bg{position:absolute;inset:0;background-image:linear-gradient(#ffffff08 1px,transparent 1px),linear-gradient(90deg,#ffffff08 1px,transparent 1px);background-size:40px 40px}
.hero-inner{position:absolute;left:186px;top:70px;width:400px}
.hero h1{font-weight:900;font-size:49px;line-height:1.06;letter-spacing:-.03em;margin-top:18px}
.hero h1 em{font-style:normal;color:var(--red)}
.hero p{margin-top:24px;font-size:12.5px;line-height:1.6;color:#c4c4ca}
.hero .ctas{margin-top:26px;display:flex;gap:14px}
.hero .facts{margin-top:30px;display:flex;gap:40px}
.fact b{display:block;font-size:17px;font-weight:700}
.fact span{display:block;margin-top:6px;font-size:7px;color:var(--dim)}
.hero-photo{position:absolute;left:681px;top:105px;width:333px;height:365px;background:linear-gradient(160deg,#2a3638 0%,#1d6f6a 35%,#114a4a 60%,#6b6a2a 85%,#1a1a1a 100%);border:1px solid var(--line)}
.badge30{position:absolute;left:662px;top:410px;width:84px;height:84px;border-radius:50%;background:var(--red);display:flex;flex-direction:column;align-items:center;justify-content:center;box-shadow:0 10px 30px #0008}
.badge30 b{font-size:26px;font-weight:900;line-height:1}
.badge30 span{font-size:6px;margin-top:3px}

/* trust bar */
.trust{height:45px;background:var(--bg-alt);border-bottom:1px solid var(--line)}
.trust .row{width:830px;margin:0 auto;height:45px;display:flex;align-items:center;gap:24px;font-size:8.5px;color:#c4c4ca}
.trust .row .mono{font-size:7px;color:var(--dim);margin-right:auto}
.trust .item{display:flex;gap:6px;align-items:center}
.trust svg{width:10px;height:10px;stroke:var(--red);fill:none;stroke-width:1.8}

/* services */
.services{height:860px;padding-top:75px}
.services h2{margin-top:12px;width:470px}
.services .lede{margin-top:14px;width:460px;font-size:11px;line-height:1.6;color:var(--muted)}
.svc-grid{margin-top:40px;display:grid;grid-template-columns:repeat(4,1fr);border:1px solid var(--line)}
.svc{height:198px;padding:22px 20px;border-right:1px solid var(--line);border-bottom:1px solid var(--line);position:relative;background:var(--bg)}
.svc:nth-child(4n){border-right:0}
.svc:nth-child(n+5){border-bottom:0}
.svc .num{position:absolute;right:16px;top:14px;font-family:"IBM Plex Mono",monospace;font-size:8px;color:var(--dim)}
.svc h3{margin-top:18px;font-size:12.5px;font-weight:700}
.svc p{margin-top:8px;font-size:9px;line-height:1.55;color:var(--muted)}
.svc .tags{margin-top:12px;font-size:7px;color:var(--dim)}
.scope{margin-top:18px;height:138px;background:var(--panel);border:1px solid var(--line);display:flex;padding:30px 28px}
.scope .lead{width:215px}
.scope .lead .mono{font-size:7px;color:var(--dim)}
.scope .lead h4{margin-top:10px;font-size:14px;font-weight:700}
.scope .lead p{margin-top:8px;font-size:8.5px;line-height:1.55;color:var(--muted)}
.scope ul{list-style:none;display:grid;grid-template-columns:repeat(3,1fr);gap:14px 20px;flex:1}
.scope li{display:flex;gap:8px}
.scope li b{display:block;font-size:9.5px;font-weight:600}
.scope li span{display:block;margin-top:3px;font-size:7.5px;line-height:1.45;color:var(--muted)}

/* serve */
.serve{height:529px;background:var(--bg-alt);border-top:1px solid var(--line);border-bottom:1px solid var(--line);padding-top:77px;text-align:center}
.serve h2{margin-top:12px}
.serve-grid{margin-top:38px;display:grid;grid-template-columns:repeat(3,1fr);gap:18px;text-align:left}
.tier{height:258px;padding:28px 24px;background:var(--bg);border:1px solid var(--line);position:relative}
.tier.hot{border-color:var(--red);background:linear-gradient(180deg,#2a1214,#17121a 70%)}
.tier .flag{position:absolute;top:0;right:20px;background:var(--red);font-size:6.5px;padding:4px 8px;font-family:"IBM Plex Mono",monospace;letter-spacing:.12em}
.tier h3{margin-top:18px;font-size:14px;font-weight:700}
.tier p{margin-top:8px;font-size:9px;line-height:1.6;color:var(--muted)}
.tier ul{list-style:none;margin-top:22px}
.tier li{display:flex;gap:10px;align-items:center;font-size:8.5px;color:#c4c4ca;margin-bottom:11px}

/* why */
.why{height:760px;padding-top:75px}
.why-row{display:flex;gap:48px}
.why-photo{width:369px;height:422px;background:linear-gradient(150deg,#c9c7c0 0%,#8a7b4a 30%,#3d3b34 55%,#1e2a34 80%,#14171c 100%);position:relative}
.why-photo .cap{position:absolute;left:14px;bottom:12px;font-size:7px;color:#ddd}
.why-copy{flex:1;padding-top:2px}
.why-copy h2{margin-top:12px}
.point{display:flex;gap:14px;padding:20px 0;border-bottom:1px solid var(--line)}
.point:first-of-type{margin-top:14px}
.point .icon-box{width:22px;height:22px;flex:none}
.point b{font-size:10.5px;font-weight:600}
.point p{margin-top:6px;font-size:8.5px;line-height:1.6;color:var(--muted)}
.stats{margin-top:42px;display:grid;grid-template-columns:repeat(4,1fr);border-top:1px solid var(--line);border-bottom:1px solid var(--line)}
.stat{height:160px;text-align:center;padding-top:30px;border-right:1px solid var(--line)}
.stat:last-child{border-right:0}
.stat b{font-size:38px;font-weight:800;letter-spacing:-.02em}
.stat i{display:block;width:4px;height:4px;background:var(--red);border-radius:50%;margin:10px auto}
.stat span{font-size:7px;color:var(--dim)}

/* process */
.process{height:380px;padding-top:34px;text-align:center}
.process h2{margin-top:12px}
.steps{margin-top:38px;display:grid;grid-template-columns:repeat(4,1fr);background:var(--panel);border:1px solid var(--line);text-align:left}
.step{height:156px;padding:24px 20px;border-right:1px solid var(--line)}
.step:last-child{border-right:0}
.step .mono{font-size:8px;color:var(--red);letter-spacing:.08em}
.step h3{margin-top:16px;font-size:12.5px;font-weight:700}
.step p{margin-top:9px;font-size:8.5px;line-height:1.6;color:var(--muted)}

/* reviews */
.reviews{height:506px;background:var(--bg-alt);border-top:1px solid var(--line);border-bottom:1px solid var(--line);padding-top:78px;text-align:center}
.reviews h2{margin-top:12px}
.rev-grid{margin-top:40px;display:grid;grid-template-columns:repeat(3,1fr);text-align:left;border-top:1px solid var(--line);border-bottom:1px solid var(--line)}
.rev{height:200px;padding:22px 22px;border-right:1px solid var(--line)}
.rev:last-child{border-right:0}
.stars{color:var(--red);font-size:11px;letter-spacing:3px}
.rev q{display:block;margin-top:14px;font-size:10px;line-height:1.7;color:#d0d0d5;quotes:"\201C" "\201D"}
.who{margin-top:26px;display:flex;gap:12px;align-items:center}
.who i{width:26px;height:26px;border-radius:50%;border:1px solid var(--line);display:flex;align-items:center;justify-content:center;font-style:normal;font-size:9px;color:var(--red)}
.who b{display:block;font-size:9.5px;font-weight:600}
.who span{display:block;margin-top:4px;font-size:6.5px;color:var(--dim)}
.rating{margin-top:20px;font-size:7px;color:var(--dim);display:flex;align-items:center;justify-content:center;gap:8px}
.rating i{width:8px;height:8px;border-radius:50%;background:var(--muted);display:block}

/* contact */
.contact{height:582px;background:radial-gradient(ellipse at 85% 0%,#3a1214 0%,transparent 50%),var(--bg-deep);padding-top:78px}
.contact-row{display:flex;gap:74px}
.contact-left{width:354px}
.contact-left h2{margin-top:12px;font-size:33px}
.contact-left .lede{margin-top:18px;font-size:10.5px;line-height:1.6;color:var(--muted)}
.crow{display:flex;gap:16px;padding:20px 0;border-bottom:1px solid var(--line)}
.crow:first-of-type{margin-top:22px;border-top:1px solid var(--line)}
.crow svg{width:14px;height:14px;stroke:var(--red);fill:none;stroke-width:1.6;margin-top:6px}
.crow .mono{font-size:6.5px;color:var(--dim)}
.crow b{display:block;margin-top:4px;font-size:11px;font-weight:600}
.crow span{display:block;margin-top:4px;font-size:8px;color:var(--muted)}
.form{flex:1;background:var(--panel);border:1px solid var(--line);padding:24px 0 0;margin-top:-12px;height:470px}
.form .inner{padding:0 0 0 0;width:316px;margin-left:0}
.form{padding-left:24px;padding-right:24px}
.form h3{margin-top:8px;font-size:14px;font-weight:700}
.fgrid{margin-top:20px;display:grid;grid-template-columns:1fr 1fr;gap:14px 14px}
.field label{display:block;font-size:7.5px;color:#c4c4ca;margin-bottom:6px}
.field label em{color:var(--red);font-style:normal}
.field .in{height:28px;background:var(--bg-deep);border:1px solid var(--line);font-size:8.5px;color:var(--dim);padding:0 10px;display:flex;align-items:center}
.field.full{grid-column:1/3}
.field .in.sel{justify-content:space-between;color:var(--text)}
.field .in.area{height:62px;align-items:flex-start;padding-top:10px;line-height:1.4}
.form .btn{margin-top:20px;width:100%;justify-content:center;height:36px}
.form .note{margin-top:14px;text-align:center;font-size:6.5px;color:var(--dim)}

/* footer */
.footer{height:281px;background:var(--bg);border-top:1px solid var(--line);padding-top:56px}
.foot-row{display:flex}
.foot-brand{width:250px}
.foot-brand p{margin-top:16px;font-size:8.5px;line-height:1.7;color:var(--muted);width:200px}
.foot-col{width:186px}
.foot-col .mono{font-size:7px;color:var(--dim)}
.foot-col ul{list-style:none;margin-top:14px}
.foot-col li{font-size:8.5px;color:var(--muted);margin-bottom:9px;line-height:1.5}
.foot-base{margin-top:60px;border-top:1px solid var(--line);padding-top:16px;display:flex;justify-content:space-between;font-size:7px;color:var(--dim)}
</style>
</head>
<body>

<header class="nav">
  <div class="wrap">
    <div class="logo"><i></i>Wirelumo</div>
    <ul><li>Services</li><li>Why Us</li><li>Process</li><li>Reviews</li><li>Contact</li></ul>
    <div class="phone"><svg viewBox="0 0 24 24"><path d="M5 3h4l2 5-3 2a12 12 0 0 0 6 6l2-3 5 2v4a2 2 0 0 1-2 2A17 17 0 0 1 3 5a2 2 0 0 1 2-2z"/></svg>(888) 555-0142</div>
    <span class="btn btn-red">Request a Quote</span>
  </div>
</header>

<section class="hero">
  <div class="grid-bg"></div>
  <div class="hero-inner">
    <div class="eyebrow">Commercial Low-Voltage · VA · DC · MD</div>
    <h1>The infrastructure your business <em>runs on.</em></h1>
    <p>Structured cabling, surveillance, access control and connectivity — engineered, installed and certified for commercial and industrial facilities. Thirty years of doing it right the first time.</p>
    <div class="ctas">
      <span class="btn btn-red">Request a Quote <svg width="10" height="10" viewBox="0 0 24 24" fill="none" stroke="#fff" stroke-width="2.4"><path d="M5 12h14M13 6l6 6-6 6"/></svg></span>
      <span class="btn btn-ghost"><svg width="11" height="11" viewBox="0 0 24 24" fill="none" stroke="#fff" stroke-width="1.8"><path d="M5 3h4l2 5-3 2a12 12 0 0 0 6 6l2-3 5 2v4a2 2 0 0 1-2 2A17 17 0 0 1 3 5a2 2 0 0 1 2-2z"/></svg>(888) 555-0142</span>
    </div>
    <div class="facts">
      <div class="fact"><b>Est. 1995</b><span class="mono">30 years in business</span></div>
      <div class="fact"><b>Veritest Certified</b><span class="mono">VX-8000 testing</span></div>
      <div class="fact"><b>1-Hour</b><span class="mono">Quote response</span></div>
    </div>
  </div>
  <div class="hero-photo" role="img" aria-label="Server rack with neatly dressed teal and yellow network patch cables"></div>
  <div class="badge30"><b>30</b><span class="mono">Years · 1995–2025</span></div>
</section>

<div class="trust">
  <div class="row">
    <span class="mono">Trusted by commercial &amp; industrial clients across the DMV</span>
    <span class="item"><svg viewBox="0 0 24 24"><path d="M12 3l8 3v6c0 5-4 8-8 9-4-1-8-4-8-9V6z"/></svg>Licensed &amp; Insured</span>
    <span class="item"><svg viewBox="0 0 24 24"><circle cx="12" cy="12" r="9"/><path d="M12 7v5l3 2"/></svg>24/7 Support</span>
    <span class="item"><svg viewBox="0 0 24 24"><path d="M3 17l6-6 4 4 8-8"/></svg>CTSA Best Practices</span>
    <span class="item"><svg viewBox="0 0 24 24"><circle cx="12" cy="12" r="9"/><path d="M8 12l3 3 5-6"/></svg>Works With Your IT Team</span>
  </div>
</div>

<section class="services">
  <div class="wrap">
    <div class="eyebrow">What we do</div>
    <h2>One contractor for every low-voltage system in your building.</h2>
    <p class="lede">From the riser to the rack to the rooftop dish — we design, install, terminate and certify the systems that keep commercial operations connected and secure.</p>
    <div class="svc-grid">
      <div class="svc"><span class="num">01</span><div class="icon-box"><svg viewBox="0 0 24 24"><circle cx="12" cy="5" r="2"/><circle cx="5" cy="19" r="2"/><circle cx="19" cy="19" r="2"/><path d="M12 7v5M5 17v-5h14v5"/></svg></div><h3>Structured Cabling</h3><p>CAT6 / CAT6A / CAT7 copper backbone and horizontal cabling, IDF/MDF buildouts and clean cable management.</p><div class="tags mono">Copper · Voice &amp; Data →</div></div>
      <div class="svc"><span class="num">02</span><div class="icon-box"><svg viewBox="0 0 24 24"><path d="M3 12h6l3-4 3 8 3-4h3"/></svg></div><h3>Fiber Optic</h3><p>Single-mode and multimode fiber installation, fusion splicing, termination and OTDR testing for high-bandwidth links.</p><div class="tags mono">SM · MM · Splicing →</div></div>
      <div class="svc"><span class="num">03</span><div class="icon-box"><svg viewBox="0 0 24 24"><rect x="3" y="7" width="13" height="10"/><path d="M16 11l5-3v8l-5-3"/></svg></div><h3>Video Surveillance</h3><p>IP camera systems, NVR/VMS, PoE infrastructure and remote monitoring designed to cover every blind spot.</p><div class="tags mono">IP CCTV · NVR →</div></div>
      <div class="svc"><span class="num">04</span><div class="icon-box"><svg viewBox="0 0 24 24"><circle cx="8" cy="15" r="4"/><path d="M11 12l9-9M17 6l3 3"/></svg></div><h3>Access Control</h3><p>Card, fob and mobile credential systems, electric strikes and maglocks, with integration into your existing directory.</p><div class="tags mono">Cards · Mobile · Maglock →</div></div>
      <div class="svc"><span class="num">05</span><div class="icon-box"><svg viewBox="0 0 24 24"><path d="M2 9a15 15 0 0 1 20 0M5 13a10 10 0 0 1 14 0M9 17a4 4 0 0 1 6 0"/><circle cx="12" cy="20" r=".6"/></svg></div><h3>Wireless Access Points</h3><p>Predictive Wi-Fi design, heat-mapping and WAP installation for full-coverage, high-density commercial environments.</p><div class="tags mono">Wi-Fi 6/6E · Heat-map →</div></div>
      <div class="svc"><span class="num">06</span><div class="icon-box"><svg viewBox="0 0 24 24"><rect x="3" y="6" width="18" height="12"/><path d="M3 10h18"/></svg></div><h3>Point of Sale</h3><p>Dedicated cabling and network drops for POS terminals, kiosks and payment hardware across retail and hospitality.</p><div class="tags mono">Retail · Hospitality →</div></div>
      <div class="svc"><span class="num">07</span><div class="icon-box"><svg viewBox="0 0 24 24"><path d="M5 19a9 9 0 0 1 0-13l13 13a9 9 0 0 1-13 0zM14 10l5-5M17 3l4 4"/></svg></div><h3>OrbitNet Installation</h3><p>Professional mounting, weatherproofing and network integration for OrbitNet — primary or failover connectivity anywhere.</p><div class="tags mono">Mount · Failover →</div></div>
      <div class="svc"><span class="num">08</span><div class="icon-box"><svg viewBox="0 0 24 24"><rect x="3" y="4" width="18" height="12"/><path d="M9 20h6M12 16v4"/></svg></div><h3>Conference Room Tech</h3><p>Displays, video conferencing, audio and control systems — fully cabled and commissioned meeting spaces.</p><div class="tags mono">AV · VC · Control →</div></div>
    </div>
    <div class="scope">
      <div class="lead"><div class="mono">— Full scope</div><h4>Included on <span style="color:var(--text)">every</span> project.</h4><p>We handle the whole job end-to-end — not just the cable pull.</p></div>
      <ul>
        <li><svg class="tick" viewBox="0 0 24 24"><path d="M4 12l5 5 11-11"/></svg><div><b>Cabling</b><span>Copper &amp; fiber pulls, terminations</span></div></li>
        <li><svg class="tick" viewBox="0 0 24 24"><path d="M4 12l5 5 11-11"/></svg><div><b>Wi-Fi</b><span>WAP design, heat-mapping &amp; setup</span></div></li>
        <li><svg class="tick" viewBox="0 0 24 24"><path d="M4 12l5 5 11-11"/></svg><div><b>IDF / MDF</b><span>Telecom closet buildouts</span></div></li>
        <li><svg class="tick" viewBox="0 0 24 24"><path d="M4 12l5 5 11-11"/></svg><div><b>Racking</b><span>Server &amp; network rack install</span></div></li>
        <li><svg class="tick" viewBox="0 0 24 24"><path d="M4 12l5 5 11-11"/></svg><div><b>Certifications</b><span>Veritest VX-8000 testing &amp; reports</span></div></li>
        <li><svg class="tick" viewBox="0 0 24 24"><path d="M4 12l5 5 11-11"/></svg><div><b>Low-Voltage Permits</b><span>Pulled &amp; managed for you</span></div></li>
      </ul>
    </div>
  </div>
</section>

<section class="serve">
  <div class="wrap">
    <div class="eyebrow center">Who we serve</div>
    <h2>Three environments. One<br>trusted cabling partner.</h2>
    <div class="serve-grid">
      <div class="tier"><div class="icon-box"><svg viewBox="0 0 24 24"><path d="M3 11l9-7 9 7v9H3z"/><path d="M10 20v-6h4v6"/></svg></div><h3>Residential</h3><p>Smart-home cabling and whole-home Wi-Fi for all your devices, entertainment and security systems.</p><ul><li><svg class="tick" viewBox="0 0 24 24"><path d="M4 12l5 5 11-11"/></svg>Whole-home Wi-Fi &amp; mesh</li><li><svg class="tick" viewBox="0 0 24 24"><path d="M4 12l5 5 11-11"/></svg>Smart-home &amp; AV wiring</li><li><svg class="tick" viewBox="0 0 24 24"><path d="M4 12l5 5 11-11"/></svg>Cameras &amp; door access</li></ul></div>
      <div class="tier hot"><span class="flag">MOST REQUESTED</span><div class="icon-box"><svg viewBox="0 0 24 24"><rect x="5" y="3" width="14" height="18"/><path d="M9 7h2M13 7h2M9 11h2M13 11h2M9 15h2M13 15h2"/></svg></div><h3>Commercial</h3><p>Complete office low-voltage cabling, Wi-Fi, surveillance and access control for your network and security systems.</p><ul><li><svg class="tick" viewBox="0 0 24 24"><path d="M4 12l5 5 11-11"/></svg>Structured copper &amp; fiber</li><li><svg class="tick" viewBox="0 0 24 24"><path d="M4 12l5 5 11-11"/></svg>Cameras, access &amp; POS</li><li><svg class="tick" viewBox="0 0 24 24"><path d="M4 12l5 5 11-11"/></svg>Conference room AV</li></ul></div>
      <div class="tier"><div class="icon-box"><svg viewBox="0 0 24 24"><path d="M3 21V9l6 4V9l6 4V5h6v16z"/></svg></div><h3>Industrial</h3><p>Structured cabling, IDF and MDF buildouts for warehouses, manufacturing facilities, data centers and more.</p><ul><li><svg class="tick" viewBox="0 0 24 24"><path d="M4 12l5 5 11-11"/></svg>IDF / MDF &amp; racking</li><li><svg class="tick" viewBox="0 0 24 24"><path d="M4 12l5 5 11-11"/></svg>Warehouse &amp; plant runs</li><li><svg class="tick" viewBox="0 0 24 24"><path d="M4 12l5 5 11-11"/></svg>Conduit &amp; fiber backbone</li></ul></div>
    </div>
  </div>
</section>

<section class="why">
  <div class="wrap">
    <div class="why-row">
      <div class="why-photo" role="img" aria-label="Technician seen from above working among yellow fiber and network cables"><span class="cap mono">On-site · DMV region</span></div>
      <div class="why-copy">
        <div class="eyebrow">Why Wirelumo</div>
        <h2>A full-service partner,<br>not just an installer.</h2>
        <div class="point"><div class="icon-box"><svg viewBox="0 0 24 24"><path d="M4 12l5 5 11-11"/></svg></div><div><b>30 years, every size of job</b><p>From a single office to a multi-building campus or industrial warehouse — no project is too big or too small.</p></div></div>
        <div class="point"><div class="icon-box"><svg viewBox="0 0 24 24"><path d="M4 12l5 5 11-11"/></svg></div><div><b>Certified &amp; tested workmanship</b><p>Every run is Veritest VX-8000 certified and documented, so you have proof of performance — not just a promise.</p></div></div>
        <div class="point"><div class="icon-box"><svg viewBox="0 0 24 24"><path d="M4 12l5 5 11-11"/></svg></div><div><b>We work with your IT team</b><p>We coordinate directly with your staff and stay until everything is up, tested and running after installation.</p></div></div>
        <div class="point"><div class="icon-box"><svg viewBox="0 0 24 24"><path d="M4 12l5 5 11-11"/></svg></div><div><b>Honest, local &amp; responsive</b><p>A local DMV team that answers the phone, shows up on schedule and gives you a quote within the hour.</p></div></div>
      </div>
    </div>
    <div class="stats">
      <div class="stat"><b>30</b><i></i><span class="mono">Years in business</span></div>
      <div class="stat"><b>2,500</b><i></i><span class="mono">Projects completed</span></div>
      <div class="stat"><b>4.9</b><i></i><span class="mono">Review rating</span></div>
      <div class="stat"><b>3</b><i></i><span class="mono">States served · VA DC MD</span></div>
    </div>
  </div>
</section>

<section class="process">
  <div class="wrap">
    <div class="eyebrow center">How we work</div>
    <h2>A clean, predictable<br>install — start to finish.</h2>
    <div class="steps">
      <div class="step"><div class="mono">01 / Assess</div><h3>Site Walk &amp; Design</h3><p>We survey the facility, map your needs and engineer a cabling and systems plan built to code and to scale.</p></div>
      <div class="step"><div class="mono">02 / Quote</div><h3>Clear Proposal</h3><p>A detailed, transparent quote within the hour — scope, materials and timeline with no surprises.</p></div>
      <div class="step"><div class="mono">03 / Install</div><h3>Clean Installation</h3><p>Tidy, labeled, code-compliant runs installed with minimal disruption to your daily operations.</p></div>
      <div class="step"><div class="mono">04 / Certify</div><h3>Test &amp; Hand-off</h3><p>Veritest certification, full documentation and a walkthrough with your IT team before we close out.</p></div>
    </div>
  </div>
</section>

<section class="reviews">
  <div class="wrap">
    <div class="eyebrow center">Client reviews</div>
    <h2>Commercial clients<br>keep calling us back.</h2>
    <div class="rev-grid">
      <div class="rev"><div class="stars">★★★★★</div><q>Wirelumo ran our entire office network and camera system. Clean work, fully labeled, and certified. They coordinated with our IT vendor without a single hiccup.</q><div class="who"><i>O</i><div><b>Owen P.</b><span class="mono">Operations Director · Tysons, VA</span></div></div></div>
      <div class="rev"><div class="stars">★★★★★</div><q>We needed a warehouse re-cabled fast during a move. They scoped it same-day, quoted within an hour, and finished ahead of schedule. Total pros.</q><div class="who"><i>L</i><div><b>Lena K.</b><span class="mono">Facilities Manager · Beltsville, MD</span></div></div></div>
      <div class="rev"><div class="stars">★★★★★</div><q>Installed our cameras, access control and conference room AV in one coordinated project. Everything just works, and the documentation was excellent.</q><div class="who"><i>P</i><div><b>Priya N.</b><span class="mono">IT Manager · Washington, DC</span></div></div></div>
    </div>
    <div class="rating mono"><i></i>Rated 4.9 / 5 across verified reviews</div>
  </div>
</section>

<section class="contact">
  <div class="wrap">
    <div class="contact-row">
      <div class="contact-left">
        <div class="eyebrow">Get started</div>
        <h2>Let's scope<br>your project.</h2>
        <p class="lede">Tell us about your facility and what you need wired, secured or connected. We'll get back to you with a quote within the hour.</p>
        <div class="crow"><svg viewBox="0 0 24 24"><path d="M5 3h4l2 5-3 2a12 12 0 0 0 6 6l2-3 5 2v4a2 2 0 0 1-2 2A17 17 0 0 1 3 5a2 2 0 0 1 2-2z"/></svg><div><div class="mono">Call us</div><b>(888) 555-0142</b><span>Local: 703-555-0190</span></div></div>
        <div class="crow"><svg viewBox="0 0 24 24"><rect x="3" y="5" width="18" height="14"/><path d="M3 6l9 7 9-7"/></svg><div><div class="mono">Email</div><b>sales@wirelumo.com</b></div></div>
        <div class="crow"><svg viewBox="0 0 24 24"><path d="M12 21s-7-6-7-11a7 7 0 0 1 14 0c0 5-7 11-7 11z"/><circle cx="12" cy="10" r="2.5"/></svg><div><div class="mono">Office</div><b>4120 Larkspur Way, Suite 310</b><span>Fairview, VA 22030 · Serving VA · DC · MD</span></div></div>
      </div>
      <div class="form">
        <div class="eyebrow">Request a quote</div>
        <h3>Get a response within the hour.</h3>
        <div class="fgrid">
          <div class="field"><label>Name <em>*</em></label><div class="in">Jane Smith</div></div>
          <div class="field"><label>Company</label><div class="in">Acme Inc.</div></div>
          <div class="field"><label>Email <em>*</em></label><div class="in">jane@company.com</div></div>
          <div class="field"><label>Phone</label><div class="in">(555) 555-5555</div></div>
          <div class="field full"><label>Service Needed</label><div class="in sel">Structured Cabling (Copper)<svg width="8" height="8" viewBox="0 0 24 24" fill="none" stroke="#9a9aa2" stroke-width="2.5"><path d="M6 9l6 6 6-6"/></svg></div></div>
          <div class="field full"><label>Project Details <em>*</em></label><div class="in area">Tell us about your facility, square footage, timeline, and what you need installed.</div></div>
        </div>
        <span class="btn btn-red">Request Call Back <svg width="10" height="10" viewBox="0 0 24 24" fill="none" stroke="#fff" stroke-width="2.4"><path d="M5 12h14M13 6l6 6-6 6"/></svg></span>
        <div class="note mono">No spam. We only use your info to scope your project.</div>
      </div>
    </div>
  </div>
</section>

<footer class="footer">
  <div class="wrap">
    <div class="foot-row">
      <div class="foot-brand"><div class="logo"><i></i>Wirelumo</div><p>A local group of IT professionals delivering fast, reliable and honest low-voltage cabling and systems for commercial and industrial clients across Virginia, Washington DC and Maryland.</p></div>
      <div class="foot-col"><div class="mono">Services</div><ul><li>Structured Cabling</li><li>Fiber Optic</li><li>Video Surveillance</li><li>Access Control</li><li>Wireless / WAP</li></ul></div>
      <div class="foot-col"><div class="mono">Company</div><ul><li>Why Wirelumo</li><li>Our Process</li><li>Reviews</li><li>Contact</li></ul></div>
      <div class="foot-col"><div class="mono">Contact</div><ul><li>(888) 555-0142</li><li>sales@wirelumo.com</li><li>4120 Larkspur Way, Ste 310<br>Fairview, VA 22030</li></ul></div>
    </div>
    <div class="foot-base mono"><span>© 2025 Wirelumo · Licensed &amp; Insured</span><span>Serving VA · DC · MD</span></div>
  </div>
</footer>

</body>
</html>
```